Business Card for Technology Startup

Design a 2-sided business card using the logo provided. We are a digital healthcare platform that provides a mobile app and web UI that helps caregivers, families, and doctors share information and provide better patient outcomes. We use AI and machine learning to help guide patients through their day-to-day life. The final design should communicate stability, peace, comfort, but also align with the image of an AI-driven technology startup.

I'd like the deliverable to by a Photoshop PSD file (with layers) that I can work with in pixlr.com. Should contain the following editable layers:
Name (ex. John Doe)
Title (ex. Founder / CEO)
Email (ex. info@brenvaxa.ai)
Phone (ex. (555) 210-4863)
Website (ex. https://brenvaxa.ai)

```html
<!DOCTYPE html>
<html lang="en">
<head>
<meta charset="utf-8">
<title>Brenvaxa Business Card</title>
<link href="https://fonts.googleapis.com/css2?family=Poppins:wght@300;400;600;700&display=swap" rel="stylesheet">
<style>
  :root {
    --page: #2b2c2e;
    --card: #1e2125;
    --card-soft: #272a2e;
    --card-softer: #2c2f33;
    --white: #ffffff;
    --muted: #e6e8ea;
    --accent: #1fb8e6;
    --accent-light: #5fd0ea;
  }
  * { margin: 0; padding: 0; box-sizing: border-box; }
  html, body {
    width: 1200px;
    height: 1189px;
    overflow: hidden;
    background: var(--page);
    font-family: "Poppins", sans-serif;
  }
  .canvas {
    position: relative;
    width: 1200px;
    height: 1189px;
  }
  .card {
    position: absolute;
    left: 150px;
    width: 900px;
    height: 514px;
    background: var(--card);
    border-radius: 30px;
    overflow: hidden;
    box-shadow: 0 18px 40px rgba(0,0,0,0.45);
  }
  .card--front { top: 60px; }
  .card--back { top: 615px; }

  .front-shapes {
    position: absolute;
    inset: 0;
  }

  .front-brand {
    position: absolute;
    left: 0;
    right: 0;
    top: 50%;
    transform: translateY(-50%);
    display: flex;
    align-items: center;
    justify-content: center;
    gap: 22px;
  }
  .brand-dot {
    width: 46px;
    height: 46px;
    border-radius: 50%;
    background: linear-gradient(135deg, var(--accent), var(--accent-light));
  }
  .brand-name {
    color: var(--white);
    font-weight: 700;
    font-size: 88px;
    letter-spacing: 1px;
    line-height: 1;
  }

  .back-accent {
    position: absolute;
    left: 150px;
    top: 170px;
    width: 170px;
    height: 170px;
    border-radius: 50%;
    background: linear-gradient(135deg, var(--accent), var(--accent-light));
  }

  .back-details {
    position: absolute;
    left: 470px;
    top: 125px;
  }
  .back-brand {
    color: var(--white);
    font-weight: 700;
    font-size: 58px;
    line-height: 1;
    letter-spacing: 1px;
  }
  .person-name {
    margin-top: 20px;
    color: var(--accent);
    font-weight: 700;
    font-size: 32px;
    line-height: 1.1;
  }
  .person-title {
    color: var(--muted);
    font-weight: 300;
    font-size: 25px;
    line-height: 1.2;
  }
  .contact-list {
    list-style: none;
    margin-top: 24px;
  }
  .contact-item {
    display: flex;
    align-items: center;
    gap: 14px;
    color: var(--muted);
    font-weight: 300;
    font-size: 23px;
    line-height: 1.5;
  }
  .contact-icon {
    width: 22px;
    height: 22px;
    flex: none;
  }
</style>
</head>
<body>
<main class="canvas">

  <section class="card card--front" aria-label="Card front">
    <svg class="front-shapes" width="900" height="514" viewBox="0 0 900 514" aria-hidden="true">
      <circle cx="230" cy="40" r="120" fill="var(--card-soft)"/>
      <circle cx="150" cy="370" r="150" fill="var(--card-soft)"/>
      <circle cx="260" cy="560" r="140" fill="var(--card-softer)"/>
    </svg>
    <div class="front-brand">
      <span class="brand-dot"></span>
      <span class="brand-name">brenvaxa</span>
    </div>
  </section>

  <section class="card card--back" aria-label="Card back">
    <div class="back-accent"></div>
    <div class="back-details">
      <div class="back-brand">brenvaxa</div>
      <div class="person-name">John Doe</div>
      <div class="person-title">Founder / CEO</div>
      <ul class="contact-list">
        <li class="contact-item">
          <svg class="contact-icon" viewBox="0 0 24 24" aria-hidden="true">
            <rect x="4" y="3" width="16" height="18" rx="2" fill="none" stroke="var(--accent)" stroke-width="2.4"/>
          </svg>
          <span>(555) 210-4863</span>
        </li>
        <li class="contact-item">
          <svg class="contact-icon" viewBox="0 0 24 24" aria-hidden="true">
            <rect x="2" y="5" width="20" height="14" fill="var(--accent)"/>
            <path d="M2 5 L12 13 L22 5" fill="none" stroke="var(--card)" stroke-width="1.8"/>
          </svg>
          <span>info@brenvaxa.ai</span>
        </li>
        <li class="contact-item">
          <svg class="contact-icon" viewBox="0 0 24 24" aria-hidden="true">
            <circle cx="12" cy="12" r="9" fill="none" stroke="var(--accent)" stroke-width="2"/>
            <ellipse cx="12" cy="12" rx="4" ry="9" fill="none" stroke="var(--accent)" stroke-width="1.5"/>
            <line x1="3" y1="12" x2="21" y2="12" stroke="var(--accent)" stroke-width="1.5"/>
          </svg>
          <span>https://brenvaxa.ai</span>
        </li>
      </ul>
    </div>
  </section>

</main>
</body>
</html>
```